'TOLVANTA' NEW WINE LABEL DESIGN

I am looking for an exceptional and exciting design for a wine label called 'Tolvanta' meaning 'Lookout'. The design must feature the name 'Tolvanta', and the word 'Cabernet Sauvignon' in version 1 and 'Sauvignon Blanc' in version 2. It will also need the words 'Valle Central, Chile' at the bottom of the label as a prominent piece of information as well as the vintage 2017. Please produce the work in size 80mm x 100mm. Feel free to use colour in addition to black/white and ensue that the label is easy to read on a shelf placement.
Target Market(s)
SUPERMARKETS & WINE STORES
Requirements
Must have
- EASY TO READ, USE COLOURS LIKE GREEN FOR SAUVIGNON & RED FOR CABERNET SAUVIGNON
- FULL BOTTLE SHOT MUST BE IN PROVIDED DESIGNS. ALL BOTTLE TOPS SHOULD BE QUORLAN STYLE (SCREW TOP)
- PLEASE NOTE THAT LABEL INFORMATION MUSY BE EASY TO READ I.E. VINTAGE, PLACE OF ORGIN ALTHOUGH NOT THE MAIN CONTENT MUST STILL BE CLEAR.
Nice to have
- ARTISTIC REFERENCE LINK TO NAME & ANDES BUT NOT PICTURES OF MOUNTAINS
Should not have
- PICTURES OF GRAPES
- PICTURES OF VINEYARDS
- PICTURES OF MOUNTAINS

```html
<!DOCTYPE html>
<html lang="en">
<head>
<meta charset="utf-8">
<title>Tolvanta Wine Labels</title>
<link href="https://fonts.googleapis.com/css2?family=Rye&display=swap" rel="stylesheet">
<style>
  :root {
    --page-bg: #dcdcdc;
    --paper: #f2eee3;
    --paper-shade: #e6e0d0;
    --ink: #3a2a24;
    --white-accent: #a3cf3a;
    --red-accent: #e4252a;
    --art-tone-light: #ece8dc;
    --art-tone-dark: #b9b4a8;
  }
  html, body {
    margin: 0;
    padding: 0;
    width: 1200px;
    height: 1200px;
    overflow: hidden;
    background: var(--page-bg);
  }
  .canvas {
    position: relative;
    width: 1200px;
    height: 1200px;
    display: flex;
    justify-content: center;
    align-items: center;
    gap: 80px;
  }
  .label {
    position: relative;
    width: 460px;
    height: 600px;
    font-family: "Rye", "Georgia", serif;
    color: var(--ink);
    text-align: center;
  }
  .label--blanc { --accent: var(--white-accent); }
  .label--cabernet { --accent: var(--red-accent); }
  .label__shape {
    position: absolute;
    inset: 0;
    width: 460px;
    height: 600px;
  }
  .label__shape .outer { fill: var(--paper); stroke: var(--accent); stroke-width: 10; }
  .label__shape .inner { fill: none; stroke: var(--ink); stroke-width: 4; }
  .label__content {
    position: absolute;
    inset: 0;
    display: flex;
    flex-direction: column;
    align-items: center;
  }
  .ornament {
    width: 200px;
    height: 26px;
    border-radius: 13px;
    background: linear-gradient(90deg, transparent, var(--art-tone-dark), transparent);
    opacity: 0.7;
  }
  .ornament--top { margin-top: 62px; }
  .ornament--bottom { width: 110px; height: 30px; margin-top: 18px; }
  .brand {
    margin: 22px 0 0;
    font-size: 40px;
    letter-spacing: 3px;
    line-height: 1;
  }
  .scene-art {
    margin-top: 18px;
    width: 300px;
    height: 170px;
    border-radius: 6px;
    background: linear-gradient(180deg, var(--art-tone-light) 0%, var(--art-tone-dark) 100%);
  }
  .variety {
    color: var(--accent);
    margin-top: 26px;
    line-height: 1;
  }
  .variety__first { display: block; font-size: 28px; letter-spacing: 2px; }
  .variety__main { display: block; font-size: 48px; letter-spacing: 2px; margin-top: 6px; }
  .origin {
    margin-top: 18px;
    font-size: 15px;
    letter-spacing: 1.5px;
  }
  .vintage {
    margin-top: 12px;
    font-size: 24px;
    letter-spacing: 2px;
  }
</style>
</head>
<body>
<main class="canvas">

  <section class="label label--blanc">
    <svg class="label__shape" viewBox="0 0 460 600" aria-hidden="true">
      <path class="outer" d="M45,40 Q230,0 415,40 V65 H450 V535 H415 V560 Q230,600 45,560 V535 H10 V65 H45 Z"/>
      <path class="inner" d="M58,54 Q230,18 402,54 V78 H436 V522 H402 V546 Q230,582 58,546 V522 H24 V78 H58 Z"/>
    </svg>
    <div class="label__content">
      <div class="ornament ornament--top" role="img" aria-label="Decorative flourish"></div>
      <h2 class="brand">TOLVANTA</h2>
      <div class="scene-art" role="img" aria-label="Engraved sketch of a coastal lighthouse with a cottage, trees and seagulls"></div>
      <p class="variety"><span class="variety__first">BLANC</span><span class="variety__main">SAUVIGNON</span></p>
      <p class="origin">VALLE CENTRAL, CHILE</p>
      <p class="vintage">2017</p>
      <div class="ornament ornament--bottom" role="img" aria-label="Decorative flourish"></div>
    </div>
  </section>

  <section class="label label--cabernet">
    <svg class="label__shape" viewBox="0 0 460 600" aria-hidden="true">
      <path class="outer" d="M45,40 Q230,0 415,40 V65 H450 V535 H415 V560 Q230,600 45,560 V535 H10 V65 H45 Z"/>
      <path class="inner" d="M58,54 Q230,18 402,54 V78 H436 V522 H402 V546 Q230,582 58,546 V522 H24 V78 H58 Z"/>
    </svg>
    <div class="label__content">
      <div class="ornament ornament--top" role="img" aria-label="Decorative flourish"></div>
      <h2 class="brand">TOLVANTA</h2>
      <div class="scene-art" role="img" aria-label="Pencil sketch of a lighthouse beside a house and tall trees with a seagull"></div>
      <p class="variety"><span class="variety__first">CABERNET</span><span class="variety__main">SAUVIGNON</span></p>
      <p class="origin">VALLE CENTRAL, CHILE</p>
      <p class="vintage">2017</p>
      <div class="ornament ornament--bottom" role="img" aria-label="Decorative flourish"></div>
    </div>
  </section>

</main>
</body>
</html>
```